Business card and stationery design

Harbour & Summit Planners is a leading event and conference design and management company.
Please view harbourandsummit.com.au

The business cards needs to convey:
- professionalism and competency
- exclusivity
- memorable experiences and quality

The business card needs to have the following aspects:
- double sided
- Full colour CMYK
- Printed on either high gloss matt card (designer to recommend)

For the business stationery we require:
- Letterhead with top banner and bottom footer
- A thank you card design
- a with compliments slip design
- a MS powerpoint and MS publisher client presentation slide design which includes cover page and then a standard presentation page
(Note- we do NOT require an envelope design- who sends letters these days!)

The company image is using the key colours of gold, silver and black.
A black background to the business card has been used before and is preferred although we are open to options.

Target Market(s)

High end corporations and businesses that require their events and conferences to be exceptionally well designed and managed

Industry/Entity Type

Business

Contact Information for Business Card

FRONT:

Darcy Whitlam
- Event and Conference Specialist

Mobile- +61 (0) 491 362 047
Office- 1300 586 917
darcyw@harbourandsummit.com.au

Web- harbourandsummit.com.au

BACK:

- Event and

Font styles to use
Other font styles liked:
• The logo designer used Trajan Pro Bold 3 for the font text in the logo

Requirements
Must have
• Amazing design of the following:
• - business card (double sided)
• - letterhead
• - client thank you card
• - powerpoint and publisher client presentation design files

```html
<!DOCTYPE html>
<html lang="en">
<head>
<meta charset="utf-8">
<title>Harbour &amp; Summit Planners — Business Card</title>
<link rel="stylesheet" href="https://fonts.googleapis.com/css2?family=Cinzel:wght@700&family=Open+Sans:ital,wght@0,400;0,600;1,400&display=swap">
<style>
  :root {
    --backdrop: #8f9090;
    --card-black: #030303;
    --gold: #c99a2e;
    --gold-light: #e3bf5c;
    --gold-dark: #a77a1c;
    --silver-light: #e6e7e8;
    --silver: #b9babc;
    --silver-dark: #8e8f91;
    --text-white: #f2f2f2;
    --text-grey: #a4a4a4;
    --ink: #111111;
  }
  * { margin: 0; padding: 0; box-sizing: border-box; }
  html, body {
    width: 1105px; height: 1200px; overflow: hidden;
    background: var(--backdrop);
  }
  .sheet { position: relative; width: 1105px; height: 1200px; }
  .card {
    position: absolute; left: 182px; width: 746px; height: 427px;
    overflow: hidden;
  }
  /* Front */
  .card-front { top: 119px; background: var(--card-black); }
  .front-brand {
    position: absolute; left: 40px; top: 150px; width: 300px;
    text-align: center;
  }
  .brand-dot {
    display: block; width: 56px; height: 56px; margin: 0 auto 22px;
    border-radius: 50%; background: var(--gold);
  }
  .brand-name {
    font-family: "Cinzel", serif; font-weight: 700;
    font-size: 19px; line-height: 1.3; letter-spacing: 0.5px;
    color: var(--silver-light);
  }
  .contact-block { position: absolute; left: 348px; top: 104px; }
  .person-name {
    font-family: "Open Sans", sans-serif; font-weight: 600;
    font-size: 26px; color: var(--gold); line-height: 1.2;
  }
  .person-role {
    font-family: "Open Sans", sans-serif; font-weight: 400;
    font-size: 19px; color: var(--text-grey); margin-top: 2px;
  }
  .contact-list { list-style: none; margin-top: 22px; }
  .contact-list li {
    display: flex; align-items: center; gap: 10px;
    font-family: "Open Sans", sans-serif; font-size: 18px;
    color: var(--text-white); height: 29px;
  }
  .contact-icon { width: 17px; height: 17px; flex: none; fill: var(--gold); }
  .accent-band { position: absolute; left: 0; bottom: 0; width: 100%; height: 27px; }
  /* Back */
  .card-back {
    top: 636px;
    background:
      radial-gradient(ellipse 60% 70% at 38% 35%, #f4f4f5 0%, rgba(244,244,245,0) 70%),
      linear-gradient(135deg, var(--silver) 0%, var(--silver-light) 40%, var(--silver-dark) 100%);
  }
  .back-emblem {
    position: absolute; left: 352px; top: 24px; width: 380px; height: 380px;
    border-radius: 50%; background: var(--ink);
  }
  .back-brand { position: absolute; left: 46px; top: 318px; width: 300px; text-align: center; }
  .back-brand .brand-name { color: var(--ink); }
  .back-url {
    font-family: "Open Sans", sans-serif; font-style: italic;
    font-size: 17px; color: var(--ink); margin-top: 6px;
  }
</style>
</head>
<body>
<main class="sheet">
  <section class="card card-front" aria-label="Business card front">
    <div class="front-brand">
      <span class="brand-dot"></span>
      <p class="brand-name">HARBOUR &amp; SUMMIT<br>PLANNERS</p>
    </div>
    <div class="contact-block">
      <h1 class="person-name">Darcy Whitlam</h1>
      <p class="person-role">Event and Conference Specialist</p>
      <ul class="contact-list">
        <li>
          <svg class="contact-icon" viewBox="0 0 16 16" aria-hidden="true"><path d="M4 0h8a1.5 1.5 0 0 1 1.5 1.5v13A1.5 1.5 0 0 1 12 16H4a1.5 1.5 0 0 1-1.5-1.5v-13A1.5 1.5 0 0 1 4 0zm0 2v10h8V2zm4 11a1 1 0 1 0 0 2 1 1 0 0 0 0-2z"/></svg>
          +61 (0) 491 362 047
        </li>
        <li>
          <svg class="contact-icon" viewBox="0 0 16 16" aria-hidden="true"><path d="M3.6 0.6l2.2 2.9c.4.5.3 1.2-.1 1.6L4.4 6.3c.9 2 3.3 4.4 5.3 5.3l1.2-1.3c.4-.4 1.1-.5 1.6-.1l2.9 2.2c.5.4.6 1.2.1 1.7l-1.3 1.3c-.7.7-1.8.9-2.7.5C7 14.3 1.7 9 .4 4.5.1 3.6.3 2.5 1 1.8L2 .6c.5-.5 1.2-.4 1.6 0z"/></svg>
          1300 586 917
        </li>
        <li>
          <svg class="contact-icon" viewBox="0 0 16 16" aria-hidden="true"><path d="M0 3h16v1.2L8 9 0 4.2zM0 5.6l8 4.8 8-4.8V13H0z"/></svg>
          darcyw@harbourandsummit.com.au
        </li>
        <li>
          <svg class="contact-icon" viewBox="0 0 16 16" aria-hidden="true"><path d="M8 0a8 8 0 1 0 0 16A8 8 0 0 0 8 0zm5.9 7.2h-2.5a12 12 0 0 0-1-4.8 6.1 6.1 0 0 1 3.5 4.8zM8 1.8c.7.8 1.4 2.8 1.5 5.4h-3C6.6 4.6 7.3 2.6 8 1.8zM5.6 2.4a12 12 0 0 0-1 4.8H2.1a6.1 6.1 0 0 1 3.5-4.8zM2.1 8.8h2.5c.1 1.8.4 3.5 1 4.8a6.1 6.1 0 0 1-3.5-4.8zM8 14.2c-.7-.8-1.4-2.8-1.5-5.4h3c-.1 2.6-.8 4.6-1.5 5.4zm2.4-.6c.6-1.3.9-3 1-4.8h2.5a6.1 6.1 0 0 1-3.5 4.8z"/></svg>
          harbourandsummit.com.au
        </li>
      </ul>
    </div>
    <svg class="accent-band" viewBox="0 0 746 27" preserveAspectRatio="none" aria-hidden="true">
      <defs>
        <linearGradient id="band-gold" x1="0" x2="1" y1="0" y2="0">
          <stop offset="0" stop-color="var(--gold-dark)"/>
          <stop offset="0.55" stop-color="var(--gold-light)"/>
          <stop offset="1" stop-color="var(--gold)"/>
        </linearGradient>
        <linearGradient id="band-silver" x1="0" x2="1" y1="0" y2="0">
          <stop offset="0" stop-color="var(--silver-dark)"/>
          <stop offset="0.6" stop-color="var(--silver-light)"/>
          <stop offset="1" stop-color="var(--silver)"/>
        </linearGradient>
      </defs>
      <polygon points="0,0 497,0 488,27 0,27" fill="url(#band-gold)"/>
      <polygon points="506,0 746,0 746,27 497,27" fill="url(#band-silver)"/>
    </svg>
  </section>

  <section class="card card-back" aria-label="Business card back">
    <span class="back-emblem" aria-hidden="true"></span>
    <div class="back-brand">
      <p class="brand-name">HARBOUR &amp; SUMMIT<br>PLANNERS</p>
      <p class="back-url">www.harbourandsummit.com.au</p>
    </div>
  </section>
</main>
</body>
</html>
```